Bref créative
Stationary (Branding) for Plumbing & Heating Buisness
Dorrick Haines Ltd
Use same font as used in my logo
Dorrick Haines
Unit 8 Larchmoor Ind Est.
Cwmbrellog
Glynderrow
Harrowvale
dorrick@greenvoltaria.co.uk
www.dorrickhaines.com
Looking for complete stationary with A4 letter head, business cards and so on using the logo provided. Modern, clean and eco friendly is the image we are looking for.
The font used in the logo is not final and maybe changed so please ignore that.
Would like to see the logo on the back of the card with spot UV effect.
The font in this logo is not final and may change
plumbing
renewables
heating

```html
<!DOCTYPE html>
<html lang="en">
<head>
<meta charset="utf-8">
<title>Dorrick Haines Ltd – Business Card</title>
<link rel="stylesheet" href="https://fonts.googleapis.com/css2?family=Questrial&family=Open+Sans:ital,wght@0,400;0,600;1,700&display=swap">
<style>
  :root {
    --bg: #e9eaeb;
    --card: #ffffff;
    --green: #7cc242;
    --green-dark: #5fa22c;
    --green-light: #a6d86f;
    --grey: #5d6063;
    --grey-light: #b9bcbf;
    --ink: #3b3e41;
  }
  * { box-sizing: border-box; margin: 0; padding: 0; }
  html, body { width: 1200px; height: 864px; overflow: hidden; }
  body {
    background: var(--bg);
    font-family: "Questrial", "Open Sans", sans-serif;
    color: var(--ink);
    position: relative;
  }
  .card {
    position: absolute;
    top: 276px;
    width: 530px;
    height: 312px;
    background: var(--card);
    border-radius: 18px;
    overflow: hidden;
    box-shadow: 0 10px 24px rgba(0,0,0,.18);
  }
  .card--back { left: 45px; }
  .card--front { left: 625px; }

  /* Back */
  .back-mark {
    position: absolute;
    top: 96px; left: 0; width: 100%;
    display: flex; align-items: center; justify-content: center; gap: 14px;
  }
  .back-mark__dot {
    width: 54px; height: 54px; border-radius: 50%;
    background: var(--green);
  }
  .back-mark__name {
    font-family: "Questrial", sans-serif;
    font-size: 30px;
    color: var(--green-dark);
  }
  .back-web {
    position: absolute;
    top: 228px; left: 0; width: 100%;
    text-align: center;
    font-size: 14px;
    letter-spacing: 7px;
    color: var(--grey);
  }

  /* Front */
  .front-swoosh { position: absolute; inset: 0; }
  .front-tag {
    position: absolute;
    top: 146px; right: 28px;
    font-family: "Open Sans", sans-serif;
    font-style: italic; font-weight: 700;
    font-size: 16px;
    color: var(--green);
  }
  .front-mark {
    position: absolute;
    top: 160px; left: 30px;
    display: flex; align-items: center; gap: 10px;
  }
  .front-mark__dot {
    width: 34px; height: 34px; border-radius: 50%;
    background: var(--green);
  }
  .front-mark__name {
    font-family: "Questrial", sans-serif;
    font-size: 22px;
    color: var(--grey);
  }
  .contact {
    position: absolute;
    top: 206px; left: 44px;
    list-style: none;
    font-family: "Open Sans", sans-serif;
    font-size: 11px;
    line-height: 15px;
    color: var(--grey);
  }
  .contact li {
    display: flex; align-items: flex-start; gap: 7px;
    margin-bottom: 1px;
  }
  .contact__icon {
    width: 12px; height: 12px; flex: none;
    margin-top: 1.5px;
  }
</style>
</head>
<body>

<section class="card card--back" aria-label="Card back">
  <div class="back-mark">
    <span class="back-mark__dot"></span>
    <span class="back-mark__name">Dorrick Haines</span>
  </div>
  <p class="back-web">www.dorrickhaines.com</p>
</section>

<section class="card card--front" aria-label="Card front">
  <svg class="front-swoosh" width="530" height="312" viewBox="0 0 530 312" aria-hidden="true">
    <defs>
      <linearGradient id="greenBand" x1="0" y1="0" x2="1" y2="1">
        <stop offset="0" stop-color="#a6d86f"/>
        <stop offset="1" stop-color="#6cb535"/>
      </linearGradient>
    </defs>
    <path d="M180 0 C300 30 400 105 530 118 L530 0 Z" fill="url(#greenBand)"/>
    <path d="M250 0 C340 30 430 80 530 92 L530 118 C400 105 300 30 180 0 Z" fill="#5fa22c" opacity=".35"/>
    <path d="M20 250 C140 150 330 118 530 132 L530 142 C340 132 160 165 20 250 Z" fill="#b9bcbf"/>
    <path d="M0 312 L0 300 C180 270 380 240 530 236 L530 312 Z" fill="#7cc242" opacity=".12"/>
  </svg>

  <p class="front-tag">Dorrick Haines</p>

  <div class="front-mark">
    <span class="front-mark__dot"></span>
    <span class="front-mark__name">Dorrick Haines Ltd</span>
  </div>

  <ul class="contact">
    <li>
      <svg class="contact__icon" viewBox="0 0 12 12" aria-hidden="true"><circle cx="6" cy="6" r="6" fill="#7cc242"/><path d="M6 2.5a2 2 0 0 0-2 2c0 1.6 2 4 2 4s2-2.4 2-4a2 2 0 0 0-2-2z" fill="#fff"/></svg>
      <span>Unit 8 Larchmoor Ind Est.<br>Cwmbrellog Glynderrow Harrowvale</span>
    </li>
    <li>
      <svg class="contact__icon" viewBox="0 0 12 12" aria-hidden="true"><circle cx="6" cy="6" r="6" fill="#7cc242"/><path d="M4 3h1.2l.6 1.6-.8.6a4 4 0 0 0 1.8 1.8l.6-.8L9 6.8V8a1 1 0 0 1-1 1A5 5 0 0 1 3 4a1 1 0 0 1 1-1z" fill="#fff"/></svg>
      <span>01632 960418</span>
    </li>
    <li>
      <svg class="contact__icon" viewBox="0 0 12 12" aria-hidden="true"><circle cx="6" cy="6" r="6" fill="#7cc242"/><path d="M4 3h1.2l.6 1.6-.8.6a4 4 0 0 0 1.8 1.8l.6-.8L9 6.8V8a1 1 0 0 1-1 1A5 5 0 0 1 3 4a1 1 0 0 1 1-1z" fill="#fff"/></svg>
      <span>01632 960527</span>
    </li>
    <li>
      <svg class="contact__icon" viewBox="0 0 12 12" aria-hidden="true"><circle cx="6" cy="6" r="6" fill="#7cc242"/><rect x="3" y="4" width="6" height="4" fill="#fff"/><path d="M3 4l3 2.2L9 4" fill="none" stroke="#7cc242" stroke-width=".8"/></svg>
      <span>dorrick@greenvoltaria.co.uk</span>
    </li>
    <li>
      <svg class="contact__icon" viewBox="0 0 12 12" aria-hidden="true"><circle cx="6" cy="6" r="6" fill="#7cc242"/><circle cx="6" cy="6" r="3" fill="none" stroke="#fff" stroke-width=".9"/><path d="M3 6h6M6 3c-1.4 1.6-1.4 4.4 0 6M6 3c1.4 1.6 1.4 4.4 0 6" fill="none" stroke="#fff" stroke-width=".7"/></svg>
      <span>www.dorrickhaines.com</span>
    </li>
  </ul>
</section>

</body>
</html>
```